Home Design company focused on remodel and enhancement of kitchens and bathroorms

I already have a logo designed by ArtHarbor, I now need a design for my business cards.
The company is in the remodeling and enhancement industry for homes, focusing on kitchens and bathrooms, however, we can remodel or enhance every room in a home, an office space, etc.

The company's name is VELMOR HOME DESIGN, LLC

We'll focus on clients in the Rio Grande Valley, Texas. Primarily McAllen, Edinburg, Pharr, Mission, Brownsville and South Padre Island.

The design on the business card should transmit reliability, professionalism anda bit of upscale design.

The logo is in black and white, and would like to keep it that way.

The information that needs to be printed in the business cards is:
Company's name: Velmor Home Design
Company's Logo (attached)
My name: Noel Bramwit
Address, phone and email:
2715 N Parkline Road, Ste 348
McAllen, TX 78501
(956) 555 0187
nbramwit@velmordesign.example
Website: velmordesign.example

```html
<!DOCTYPE html>
<html lang="en">
<head>
<meta charset="utf-8">
<title>Velmor Home Design — Business Card</title>
<link rel="stylesheet" href="https://fonts.googleapis.com/css2?family=Montserrat:wght@400;500;700&family=Oswald:wght@600&display=swap">
<style>
  :root {
    --surface: #3b3b3d;
    --card: #141414;
    --ink: #ffffff;
    --ink-soft: #d9d9d9;
  }
  * { box-sizing: border-box; margin: 0; padding: 0; }
  html, body { width: 1200px; height: 1095px; overflow: hidden; }
  body {
    background: var(--surface);
    font-family: "Montserrat", Arial, sans-serif;
    color: var(--ink);
    position: relative;
  }
  .card {
    position: absolute;
    left: 220px;
    width: 760px;
    height: 434px;
    background: var(--card);
    overflow: hidden;
  }
  .card--front { top: 70px; }
  .card--back { top: 590px; }

  /* Front */
  .brand {
    position: absolute;
    top: 128px;
    left: 0;
    width: 100%;
    display: flex;
    justify-content: center;
    align-items: center;
    gap: 22px;
  }
  .brand__mark {
    width: 18px;
    height: 18px;
    background: var(--ink);
  }
  .brand__rule {
    width: 2px;
    height: 96px;
    background: var(--ink);
  }
  .brand__name {
    font-weight: 500;
    font-size: 27px;
    line-height: 31px;
    letter-spacing: 7px;
    color: var(--ink);
  }
  .social {
    position: absolute;
    top: 330px;
    left: 0;
    width: 100%;
    display: flex;
    justify-content: center;
    gap: 8px;
  }
  .social__dot {
    width: 28px;
    height: 28px;
    border-radius: 50%;
    background: var(--ink);
  }

  /* Back */
  .person {
    position: absolute;
    top: 168px;
    right: 340px;
    text-align: right;
    white-space: nowrap;
  }
  .person__name {
    font-family: "Oswald", "Arial Narrow", sans-serif;
    font-weight: 600;
    font-size: 46px;
    line-height: 52px;
    letter-spacing: 1px;
  }
  .person__role {
    font-size: 14px;
    letter-spacing: 1.5px;
    color: var(--ink-soft);
  }
  .divider {
    position: absolute;
    top: 150px;
    left: 440px;
    width: 1.5px;
    height: 110px;
    background: var(--ink);
  }
  .contact {
    position: absolute;
    top: 152px;
    left: 460px;
    right: 16px;
    list-style: none;
  }
  .contact__item {
    display: flex;
    align-items: center;
    gap: 9px;
    font-size: 14px;
    line-height: 36px;
    letter-spacing: 0.3px;
    white-space: nowrap;
  }
  .contact__item--phone { letter-spacing: 3px; }
  .contact__icon { width: 15px; height: 15px; flex: none; }
  .address {
    position: absolute;
    left: 0;
    bottom: 48px;
    width: 100%;
    text-align: center;
    font-size: 15px;
    letter-spacing: 0.3px;
    white-space: nowrap;
  }
  .address__company { font-weight: 700; }
</style>
</head>
<body>
  <section class="card card--front" aria-label="Business card front">
    <div class="brand">
      <span class="brand__mark" aria-hidden="true"></span>
      <span class="brand__rule" aria-hidden="true"></span>
      <div class="brand__name">VELMOR<br>HOME<br>DESIGN</div>
    </div>
    <div class="social" aria-label="Social channels">
      <span class="social__dot"></span>
      <span class="social__dot"></span>
      <span class="social__dot"></span>
      <span class="social__dot"></span>
    </div>
  </section>

  <section class="card card--back" aria-label="Business card back">
    <div class="person">
      <div class="person__name">NOEL BRAMWIT</div>
      <div class="person__role">CEO</div>
    </div>
    <span class="divider" aria-hidden="true"></span>
    <ul class="contact">
      <li class="contact__item contact__item--phone">
        <svg class="contact__icon" viewBox="0 0 16 16" aria-hidden="true"><path fill="#fff" d="M3.2 1.2l2.3-.4 1.3 3.2-1.5 1.2c.8 1.7 2 2.9 3.7 3.7l1.2-1.5 3.2 1.3-.4 2.3c-.2.9-1 1.5-1.9 1.4C6.2 11.9 2.6 8.3 1.8 3.1c-.1-.9.5-1.7 1.4-1.9z"/></svg>
        (956) 555 0187
      </li>
      <li class="contact__item">
        <svg class="contact__icon" viewBox="0 0 16 16" aria-hidden="true"><rect x="1" y="3" width="14" height="10" fill="#fff"/><path d="M1.5 3.5L8 9l6.5-5.5" fill="none" stroke="#141414" stroke-width="1.4"/></svg>
        nbramwit@velmordesign.example
      </li>
      <li class="contact__item">
        <svg class="contact__icon" viewBox="0 0 16 16" aria-hidden="true"><g fill="none" stroke="#fff" stroke-width="1.3"><circle cx="8" cy="8" r="6.5"/><ellipse cx="8" cy="8" rx="3" ry="6.5"/><path d="M1.5 8h13M2.5 4.8h11M2.5 11.2h11"/></g></svg>
        www.velmordesign.example
      </li>
    </ul>
    <p class="address"><span class="address__company">VELMOR HOME DESIGN-</span> 2715 N Parkline Road, Ste 348, McAllen, TX 78501</p>
  </section>
</body>
</html>
```